Business Card Design

Company name is: Ridgeline Lifeguard Training, LLC. We teach CPR/AED, First Aid, Bloodborne Pathogens and other health and safety classes. Looking for an eye-catching, progressive, cutting edge design.

Industry/Entity Type

Health

Contact Information for Business Card

Tom Wexford (555.218.4073)
June Pellicott (555.862.1940)
email is info@ridgelinetraininghq.com
website is www.RidgelineTrainingHQ.com

```html
<!DOCTYPE html>
<html lang="en">
<head>
<meta charset="utf-8">
<title>Ridgeline Lifeguard Training – Business Card</title>
<link rel="stylesheet" href="https://fonts.googleapis.com/css2?family=Urbanist:wght@500;600;700&display=swap">
<style>
  :root {
    --green-deep: #14532a;
    --green: #1f6b35;
    --green-light: #3f8f3e;
    --card-top: #f4f6f3;
    --card-bottom: #e3e8e2;
    --stage: #d9dcd7;
    --ink: #1d5a2c;
  }
  * { margin: 0; padding: 0; box-sizing: border-box; }
  html, body {
    width: 1200px; height: 970px; overflow: hidden;
    background: var(--stage);
    font-family: "Urbanist", "Century Gothic", sans-serif;
  }
  .business-card {
    position: absolute; left: 100px; top: 207px;
    width: 1000px; height: 556px;
    border-radius: 28px; overflow: hidden;
    background: linear-gradient(160deg, var(--card-top), var(--card-bottom));
    box-shadow: 0 18px 40px rgba(0,0,0,0.18);
  }
  .card-shapes { position: absolute; inset: 0; }
  .brand { position: absolute; left: 48px; top: 48px; display: flex; align-items: center; gap: 24px; }
  .brand-dot {
    width: 130px; height: 130px; border-radius: 50%;
    border: 6px solid var(--green);
  }
  .brand-name {
    color: var(--ink); font-weight: 600; font-size: 40px; line-height: 1.08;
  }
  .contacts { position: absolute; left: 46px; top: 262px; color: var(--ink); }
  .person { margin-bottom: 20px; }
  .person-name { font-weight: 700; font-size: 30px; line-height: 1.2; }
  .line { display: flex; align-items: center; gap: 8px; font-size: 24px; font-weight: 500; line-height: 1.35; }
  .line svg { width: 18px; height: 18px; flex: none; }
  .web-lines { margin-top: 14px; }
</style>
</head>
<body>
  <section class="business-card">
    <svg class="card-shapes" viewBox="0 0 1000 556" aria-hidden="true">
      <circle cx="763" cy="327" r="205" fill="none" stroke="var(--green)" stroke-width="7"/>
      <path d="M0,505 L590,505 Q660,505 690,556 L0,556 Z" fill="var(--green)"/>
    </svg>

    <header class="brand">
      <div class="brand-dot"></div>
      <h1 class="brand-name">Ridgeline Lifeguard<br>Training, LLC</h1>
    </header>

    <div class="contacts">
      <div class="person">
        <p class="person-name">Tom Wexford</p>
        <p class="line">
          <svg viewBox="0 0 20 20"><path d="M5 2 L8 6 L6 8 Q8 12 12 14 L14 12 L18 15 L16 18 Q8 18 2 6 Z" fill="var(--green)"/></svg>
          (555.218.4073)
        </p>
      </div>
      <div class="person">
        <p class="person-name">June Pellicott</p>
        <p class="line">
          <svg viewBox="0 0 20 20"><path d="M5 2 L8 6 L6 8 Q8 12 12 14 L14 12 L18 15 L16 18 Q8 18 2 6 Z" fill="var(--green)"/></svg>
          (555.862.1940)
        </p>
      </div>
      <div class="web-lines">
        <p class="line">
          <svg viewBox="0 0 20 20"><rect x="2" y="4" width="16" height="12" fill="var(--green)"/><path d="M2 4 L10 11 L18 4" fill="none" stroke="#fff" stroke-width="1.5"/></svg>
          info@ridgelinetraininghq.com
        </p>
        <p class="line">
          <svg viewBox="0 0 20 20"><circle cx="10" cy="10" r="8" fill="var(--green)"/><path d="M2 10 H18 M10 2 Q5 10 10 18 M10 2 Q15 10 10 18" fill="none" stroke="#fff" stroke-width="1.2"/></svg>
          www.RidgelineTrainingHQ.com
        </p>
      </div>
    </div>
  </section>
</body>
</html>
```